Brisa Fitness Camp promo

1080 pixel x 100 pixel promo ad for a Fitness Camp (like a boot camp, but targeted at Mum's with kids at school, so not the military boot camp type of thing).

Fitness Camps are fun, in groups of up to 15 (considered small group size)

Emotive language to use...get fit...get your summer body ready...

Key is to entice people to register...

Target Market(s)

Target market - Mum's with kids at school who want to get fit again, after prioritising their family over themselves for too long!

Requirements
Must have
• - use the logo in there somewhere...can be small...
- end file to be an animated GIF with 3 layers - EDIT - UNDERSTAND you cannot submit a GIF as the end file - so 3 x JPEG's are fine.

Wording:
"Mum's Fitness Camps - register your interest here"
"TIME to get FIT for SUMMER"
"Convenient times around school drop off"

```html
<!DOCTYPE html>
<html lang="en">
<head>
<meta charset="utf-8">
<title>Brisa Fitness Camp – Summer Promo Banner</title>
<link rel="stylesheet" href="https://fonts.googleapis.com/css2?family=Arimo:wght@400;700&family=Tinos:wght@700&display=swap">
<style>
  :root {
    --sun-pale: #fff9c4;
    --sun-yellow: #ffe34a;
    --sun-orange: #f7a51c;
    --sun-deep: #ef8a12;
    --camp-red: #a3150f;
    --headline-blue: #1238d8;
    --headline-edge: #ffffff;
    --logo-red: #d21f1b;
    --logo-paper: #ffffff;
    --photo-sky: #b9cde0;
    --photo-ground: #8a96a3;
    --stars-mix-a: #f0a53a;
    --stars-mix-b: #7ab8e8;
  }
  html, body {
    margin: 0;
    padding: 0;
    width: 1200px;
    height: 111px;
    overflow: hidden;
    background: #ffffff;
  }
  .promo-banner {
    position: relative;
    width: 1200px;
    height: 111px;
    overflow: hidden;
    background:
      radial-gradient(ellipse 520px 120px at 560px 55px, var(--sun-pale) 0%, var(--sun-yellow) 45%, transparent 80%),
      linear-gradient(180deg, var(--sun-orange) 0%, var(--sun-yellow) 30%, var(--sun-yellow) 70%, var(--sun-deep) 100%);
  }
  .sun-rays {
    position: absolute;
    inset: 0;
  }
  .hero-photo {
    position: absolute;
    left: 0;
    top: 0;
    width: 300px;
    height: 111px;
    background: linear-gradient(180deg, var(--photo-sky) 0%, #d6e0ea 55%, var(--photo-ground) 100%);
    -webkit-mask-image: linear-gradient(90deg, #000 0%, #000 75%, transparent 100%);
    mask-image: linear-gradient(90deg, #000 0%, #000 75%, transparent 100%);
  }
  .stars-burst {
    position: absolute;
    left: 840px;
    top: 0;
    width: 270px;
    height: 111px;
    background: radial-gradient(ellipse at 55% 50%, var(--stars-mix-b) 0%, var(--stars-mix-a) 55%, transparent 80%);
    opacity: 0.75;
  }
  .camp-title {
    position: absolute;
    left: 281px;
    top: 6px;
    margin: 0;
    font-family: "Arimo", Arial, sans-serif;
    font-weight: 400;
    font-size: 23px;
    color: var(--camp-red);
    white-space: nowrap;
  }
  .headline {
    position: absolute;
    left: 266px;
    top: 31px;
    margin: 0;
    font-family: "Tinos", "Times New Roman", serif;
    font-weight: 700;
    font-size: 40px;
    letter-spacing: 0.2px;
    color: var(--headline-blue);
    -webkit-text-stroke: 1px var(--headline-blue);
    text-shadow:
      2px 0 0 var(--headline-edge), -2px 0 0 var(--headline-edge),
      0 2px 0 var(--headline-edge), 0 -2px 0 var(--headline-edge),
      2px 2px 0 var(--headline-edge), -2px -2px 0 var(--headline-edge),
      2px -2px 0 var(--headline-edge), -2px 2px 0 var(--headline-edge);
    white-space: nowrap;
  }
  .register-cta {
    position: absolute;
    left: 533px;
    top: 74px;
    margin: 0;
    font-family: "Arimo", Arial, sans-serif;
    font-weight: 400;
    font-size: 23px;
    color: var(--camp-red);
    white-space: nowrap;
  }
  .brand-badge {
    position: absolute;
    left: 942px;
    top: 9px;
    width: 225px;
    height: 93px;
    box-sizing: border-box;
    background: var(--logo-red);
    border-radius: 6px;
    padding: 6px;
  }
  .brand-badge__inner {
    width: 100%;
    height: 100%;
    box-sizing: border-box;
    background: var(--logo-paper);
    border-radius: 4px;
    display: flex;
    align-items: center;
    justify-content: center;
    gap: 8px;
  }
  .brand-badge__dot {
    width: 26px;
    height: 26px;
    border-radius: 50%;
    background: var(--logo-red);
    flex: none;
  }
  .brand-badge__name {
    font-family: "Arimo", Arial, sans-serif;
    font-weight: 700;
    font-size: 19px;
    color: var(--logo-red);
    white-space: nowrap;
  }
</style>
</head>
<body>
  <div class="promo-banner">
    <svg class="sun-rays" width="1200" height="111" viewBox="0 0 1200 111" aria-hidden="true">
      <g fill="#ffffff" opacity="0.18">
        <polygon points="560,55 300,-40 380,-40"/>
        <polygon points="560,55 520,-40 600,-40"/>
        <polygon points="560,55 740,-40 820,-40"/>
        <polygon points="560,55 300,160 380,160"/>
        <polygon points="560,55 520,160 600,160"/>
        <polygon points="560,55 740,160 820,160"/>
        <polygon points="560,55 960,-10 960,40"/>
        <polygon points="560,55 960,80 960,130"/>
      </g>
    </svg>

    <div class="hero-photo" role="img" aria-label="Photo of mums doing a group kettlebell workout outdoors"></div>
    <div class="stars-burst" role="img" aria-label="Burst of colourful stars"></div>

    <p class="camp-title">Mum's Fitness Camps</p>
    <h1 class="headline">"TIME to get FIT for SUMMER"</h1>
    <p class="register-cta">register your interest here</p>

    <div class="brand-badge">
      <div class="brand-badge__inner">
        <span class="brand-badge__dot" aria-hidden="true"></span>
        <span class="brand-badge__name">Brisa Fitness Camp</span>
      </div>
    </div>
  </div>
</body>
</html>
```